Enclosed Trailer Wrap for Weed Control and Fertilizer

I need a wrap design done on the 2 sides and back of a 7'H x 16' L (sides) and 7'H x 7'W (back) enclosed trailer. I have attached a design that I want it to look like (IMG 1050). I have also uploaded the logo (Logo1) that I want on the left upper portion that will cover about 3' x 3' when placed on the trailer, but I want the lettering to be in lower case (but upper case for the beginning of each word) and I want the bright green/ glowing circle around the black logo circle like seen in IMG_1050 logo. I want the lettering curved around the logo to read "Yard Keepers of Texas" on top and "In God We Trust" curved around the bottom. In the center of the trailer at the top I want the lettering "WEED CONTROL & FERTILIZER" with "Healthier, Greener Lawns!" below. I do not want the phone number included, but do want the website url "yardkeeperstx.example". I want all of the lettering in black. I want all of that on top of nice green good looking grass that fades into trees with blue sky and clouds in the background at the top. I need this done in vector format so it can be properly scaled up to take to a company to wrap the trailer. I need all files print ready. I need the design shown on the trailer, and all the separate files. Everything needs to be high resolution so it is not pixelated when scaled to size for the trailer.

We turn weed infested grass into lush, beautiful green golf course looking grass by applying weed killer and fertilizer. yardkeeperstx.example

I may also want to add a Texas state flag and/ or a cowboy. I have also attached a photo of what I may want on the back, or something to match the sides, or the Texas state flag/ cowboy.

I do like the design in IMG_1050, however I am open to other designs and would like to see more as well.

```html
<!DOCTYPE html>
<html lang="en">
<head>
<meta charset="utf-8">
<title>Yard Keepers of Texas – Trailer Wrap</title>
<link href="https://fonts.googleapis.com/css2?family=Archivo+Black&family=Roboto+Condensed:ital,wght@1,700&display=swap" rel="stylesheet">
<style>
  :root {
    --page: #e4e5e6;
    --ink: #0b0b0b;
    --halo: rgba(255,255,255,0.9);
    --sky-top: #a9cbe0;
    --sky-low: #eef1e6;
    --trees: #4f7a2e;
    --grass: #3f9a2c;
    --grass-deep: #0f7a1c;
    --gold: #c9b77a;
    --trust-green: #1fa33a;
    --glow: #37d34a;
    --frame: #111111;
  }
  * { box-sizing: border-box; margin: 0; padding: 0; }
  html, body { width: 670px; height: 1200px; overflow: hidden; }
  body { background: var(--page); position: relative; font-family: "Archivo Black", "Arial Black", sans-serif; color: var(--ink); }

  .panel { position: absolute; overflow: hidden; border: 5px solid var(--frame); }
  .panel--side { left: 20px; width: 630px; height: 276px; }
  .panel--left { top: 28px; }
  .panel--right { top: 330px; }
  .panel--back { left: 75px; top: 648px; width: 520px; height: 520px; border-width: 16px; }

  .scenery {
    position: absolute; inset: 0;
    background: linear-gradient(180deg, var(--sky-top) 0%, var(--sky-low) 26%, var(--trees) 42%, #5f8f36 52%, var(--grass) 64%, var(--grass-deep) 100%);
  }
  .swoosh { position: absolute; inset: 0; width: 100%; height: 100%; }

  .lettering { color: var(--ink); text-shadow: 0 0 3px var(--halo), 0 0 3px var(--halo), 0 0 2px var(--halo); white-space: nowrap; }

  .brand { position: absolute; display: flex; flex-direction: column; align-items: center; text-align: center; }
  .brand__name { font-size: 11px; letter-spacing: 0.3px; }
  .brand__seal { width: 96px; height: 96px; border-radius: 50%; background: var(--ink); border: 5px solid var(--glow); box-shadow: 0 0 10px var(--glow); margin: 5px 0; }
  .brand__motto { font-size: 9px; }

  .headline { position: absolute; }
  .headline__service { font-size: 17px; letter-spacing: 0.3px; }
  .headline__promise { font-size: 17px; }

  .web { position: absolute; font-size: 11px; letter-spacing: 0.4px; background: rgba(255,255,255,0.75); padding: 2px 5px; }

  .faith { position: absolute; color: var(--trust-green); line-height: 0.9; white-space: nowrap; }
  .faith__big { font-size: 30px; letter-spacing: -0.5px; }
  .faith__small { font-size: 20px; }

  .tagline { position: absolute; text-align: center; white-space: normal; }
  .tagline--script { font-family: "Roboto Condensed", "Arial Narrow", sans-serif; font-style: italic; font-weight: 700; font-size: 12px; line-height: 1.2; }
  .tagline--plain { font-size: 8px; line-height: 1.35; white-space: nowrap; }

  .door { position: absolute; left: 430px; top: 8px; width: 116px; height: 250px; border: 4px solid var(--frame); }
  .door__handle { position: absolute; left: 10px; top: 106px; width: 38px; height: 4px; background: var(--frame); }

  .rider { position: absolute; left: 290px; top: 80px; width: 150px; height: 290px; border-radius: 40px 40px 10px 10px; background: linear-gradient(180deg, #6b5640 0%, #8a5a34 55%, #5a3a22 100%); opacity: 0.85; }
  .back-headline { position: absolute; left: 0; right: 0; bottom: 22px; text-align: center; }
  .back-headline__service, .back-headline__promise { font-size: 21px; }
</style>
</head>
<body>

<section class="panel panel--side panel--left">
  <div class="scenery" role="img" aria-label="Photo of lush golf-course grass fading into trees under a blue sky with clouds"></div>
  <svg class="swoosh" viewBox="0 0 630 276" preserveAspectRatio="none" aria-hidden="true">
    <path d="M0 200 C150 150 300 230 630 170 L630 276 L0 276 Z" fill="#1c8f22" opacity="0.85"/>
    <path d="M0 240 C180 190 320 270 630 215 L630 276 L0 276 Z" fill="#0e7318"/>
    <path d="M20 250 C200 170 360 250 520 200" fill="none" stroke="var(--gold)" stroke-width="5"/>
  </svg>
  <div class="brand" style="left:12px; top:30px; width:150px;">
    <span class="brand__name lettering">Yard Keepers of Texas</span>
    <span class="brand__seal"></span>
    <span class="brand__motto lettering">In God We Trust</span>
  </div>
  <div class="headline" style="left:190px; top:40px; width:224px; text-align:right;">
    <div class="headline__service lettering" style="font-size:12px;">WEED CONTROL &amp; FERTILIZER</div>
    <div class="headline__promise lettering" style="font-size:13px;">Healthier, Greener Lawns!</div>
  </div>
  <div class="web" style="left:206px; top:96px;">www.yardkeeperstx.example</div>
  <div class="door"><span class="door__handle"></span></div>
  <div class="faith" style="left:434px; top:30px; width:108px; text-align:center;">
    <div class="faith__big" style="font-size:22px;">IN GOD</div>
    <div class="faith__small" style="font-size:15px;">WE TRUST</div>
  </div>
  <div class="tagline tagline--script lettering" style="left:432px; top:150px; width:110px; white-space:normal;">Experience Greener, Healthier Grass in the Texas Hill Country</div>
</section>

<section class="panel panel--side panel--right">
  <div class="scenery" role="img" aria-label="Photo of lush golf-course grass fading into trees under a blue sky with clouds"></div>
  <svg class="swoosh" viewBox="0 0 630 276" preserveAspectRatio="none" aria-hidden="true">
    <path d="M250 150 C400 80 520 100 630 120 L630 276 L250 276 Z" fill="#4cb81f" opacity="0.8"/>
    <path d="M0 210 C200 160 380 250 630 180 L630 276 L0 276 Z" fill="#1c8f22" opacity="0.9"/>
    <path d="M0 245 C220 200 380 270 630 220 L630 276 L0 276 Z" fill="#0e7318"/>
    <path d="M10 195 C200 150 380 190 560 170" fill="none" stroke="var(--gold)" stroke-width="5"/>
  </svg>
  <div class="brand" style="left:10px; top:28px; width:150px;">
    <span class="brand__name lettering">Yard Keepers of Texas</span>
    <span class="brand__seal"></span>
    <span class="brand__motto lettering">In God We Trust</span>
  </div>
  <div class="faith" style="right:34px; top:14px; text-align:right;">
    <div class="faith__big">IN GOD</div>
    <div class="faith__small">WE TRUST</div>
  </div>
  <div class="headline" style="left:170px; top:72px; width:400px; text-align:left;">
    <div class="headline__service lettering">WEED CONTROL &amp; FERTILIZER</div>
    <div class="headline__promise lettering">Healthier, Greener Lawns!</div>
  </div>
  <div class="web" style="left:170px; top:128px;">www.yardkeeperstx.example</div>
  <div class="tagline tagline--plain lettering" style="left:20px; top:202px; width:140px;">Experience Greener,<br>Healthier Grass In<br>the Texas Hill Country</div>
</section>

<section class="panel panel--back">
  <div class="scenery" role="img" aria-label="Photo of a green golf course with trees and a sunrise sky"></div>
  <svg class="swoosh" viewBox="0 0 488 488" preserveAspectRatio="none" aria-hidden="true">
    <path d="M0 330 C150 290 300 360 488 300 L488 488 L0 488 Z" fill="#1c8f22" opacity="0.9"/>
    <path d="M0 380 C160 330 320 400 488 350 L488 488 L0 488 Z" fill="#0e7318"/>
    <path d="M40 370 C200 300 360 370 470 300" fill="none" stroke="var(--gold)" stroke-width="6"/>
  </svg>
  <div class="rider" role="img" aria-label="Photo of a cowboy in a hat riding a brown horse"></div>
  <div class="brand" style="left:30px; top:60px; width:200px;">
    <span class="brand__name lettering" style="font-size:14px;">Yard Keepers of Texas</span>
    <span class="brand__seal" style="width:140px; height:140px; border-width:6px;"></span>
    <span class="brand__motto lettering" style="font-size:11px;">In God We Trust</span>
  </div>
  <div class="web" style="right:36px; top:336px; font-size:12px;">www.yardkeeperstx.example</div>
  <div class="back-headline">
    <div class="back-headline__service lettering">WEED CONTROL &amp; FERTILIZER</div>
    <div class="back-headline__promise lettering">Healthier, Greener Lawns!</div>
  </div>
</section>

</body>
</html>
```